Dark Comedy Movie Poster

We need a poster design for our short film BRAM that we just wrapped on.
It's a dark comedy
Bram explores the world of loneliness through the lens of a manic man-child. Bram wants nothing more than the approval of others, giving every last bit of energy to the cause. But his ravenous attempts accomplish the opposite, turning others off. His desperation is authentic, his lonliness cavernous.
Here is a link to the film
https://clipvault.example/548207316
Password: Bram42
I want you, the artist, to pitch me an idea in any way you want. I'm open to absolutely anything right now. Once I have some pitches from you all my production team and I will sort through them and pick the best fit!
-Owen

```html
<!DOCTYPE html>
<html lang="en">
<head>
<meta charset="utf-8">
<title>BRAM — Film Poster</title>
<link href="https://fonts.googleapis.com/css2?family=Cinzel:wght@400;500&display=swap" rel="stylesheet">
<style>
  :root {
    --ink-white: #ffffff;
    --sheet-light: #e6e1e4;
    --sheet-mid: #cfc8cd;
    --jacket: #2b2a2e;
    --shirt: #e4dfd8;
    --skin: #d8b49e;
  }
  html, body {
    margin: 0;
    padding: 0;
    width: 1200px;
    height: 675px;
    overflow: hidden;
    background: var(--sheet-light);
  }
  .poster {
    position: relative;
    width: 1200px;
    height: 675px;
    overflow: hidden;
    font-family: "Cinzel", serif;
    color: var(--ink-white);
  }
  .poster__photo {
    position: absolute;
    inset: 0;
    background:
      radial-gradient(ellipse 260px 300px at 860px 300px, rgba(216,180,158,0.55), rgba(216,180,158,0) 70%),
      linear-gradient(90deg,
        var(--shirt) 0%,
        var(--shirt) 3%,
        var(--jacket) 9%,
        var(--jacket) 14%,
        var(--shirt) 17%,
        var(--shirt) 20%,
        var(--jacket) 24%,
        var(--jacket) 52%,
        var(--sheet-mid) 56%,
        var(--sheet-light) 75%,
        var(--sheet-mid) 100%);
  }
  .poster__title-block {
    position: absolute;
    left: 520px;
    top: 205px;
    width: 552px;
    text-align: center;
  }
  .poster__title {
    margin: 0;
    font-size: 196px;
    font-weight: 400;
    line-height: 1;
    letter-spacing: 14px;
    padding-left: 14px;
  }
  .poster__rule {
    height: 7px;
    background: var(--ink-white);
    margin: 36px 0 10px;
  }
  .poster__credit {
    margin: 0;
    font-size: 22px;
    line-height: 27px;
    text-decoration: underline;
    text-decoration-thickness: 1px;
    text-underline-offset: 3px;
    letter-spacing: 0.5px;
  }
  .poster__credit--cast {
    margin-top: 21px;
  }
  .poster__billing {
    position: absolute;
    left: 20px;
    right: 20px;
    bottom: 12px;
    margin: 0;
    text-align: center;
    font-size: 15.5px;
    line-height: 24px;
    letter-spacing: 0.6px;
  }
</style>
</head>
<body>
  <main class="poster">
    <div class="poster__photo" role="img" aria-label="Close-up of a groom's tuxedo with a red rose boutonniere and bow tie, with a blurred figure curled up on white bedsheets behind"></div>

    <section class="poster__title-block">
      <h1 class="poster__title">BRAM</h1>
      <div class="poster__rule"></div>
      <p class="poster__credit">Written &amp; Directed by Owen Marlow</p>
      <p class="poster__credit">Produced by Delia Fenwick</p>
      <p class="poster__credit poster__credit--cast">Starring Tobias Crane, Ruben Hale,</p>
    </section>

    <p class="poster__billing">Rest of the Credits Here - Lorem Ipsum, dolor sit amet, consectetur adipiscing elit. Sed molestie neque eget<br>lectus pulvinar euismod. Nulla sed magna elit, at lacinia tortor.</p>
  </main>
</body>
</html>
```